ONE PAGE WEB DESIGN NEEDED for Finance Company

We need a web design (ONE PAGE DESIGN ONLY) for a new finance website called Corvella Lending. Corvella Lending helps customers get the right loan, whether its a home loan, investment loan, business loan etc.

You are required to come up with just the homepage design. Professionalism and quality is the key factors in the successful design.

Here are a few design questions to help you out:

-
What information should be used on the page?
Ive provided a document which outlines all the information needed to put on homepage (attached to the brief - called corvella_page_info). Also see the Must Have section below on this brief.

-
What links should appear in the navigation/footer?:
The navigation should provide links to the following pages (NOTE: services link has subcategories):
1 Homepage
2 Services
- Home loans
- Investment loans
- Refinancing loans
- Business loans
3 About Us
4 FAQ
5 Contact Us

-
What colors should be used in the design?
Our company colors - Cyan: #2EADE3, Blue: #004B70, White. Feel free to submit designs with slight variations if you feel it improves the design.

-
What should the layout of the page be?
This is up to you to come up with - we are open to different layouts for the page design (as long as they capture the information effectively and making it easy to understand).

Target Market(s)

Potential Home owners, Families and Business Owners

Industry/Entity Type

Business

Requirements
Must have
• - Must contain our logo (attached as PNG and Illustrator file)
- Winning designer must supply a Photoshop file (PSD) that will allow us.
Nice to have
• - Should include photos/images of families, professional groups, tradespeople etc (you can use stock photos from PixelVaultImages and I will purchase them once you are selected as the winning design)
- Link to a loan calculator somewhere on front page with a button 'Find out how much you could borrow' (or maybe even try adding a loan calculator to the homepage if you think this would look good)
- Page should have a main headline "Finding the right loan for you" or "Corvella Lending finds the right loan for our customers."
- Must include Accreditation logos somewhere on the homepage (will try and supply these soon)
Should not have
• - Poor quality designs will not be considered
- Do not use clipart

```html
<!DOCTYPE html>
<html lang="en">
<head>
<meta charset="utf-8">
<title>Corvella Lending – Finding the right loan for you</title>
<link href="https://fonts.googleapis.com/css2?family=Ubuntu:wght@400;500;700&display=swap" rel="stylesheet">
<style>
:root{
  --navy:#0a3d5e;
  --navy-dark:#063350;
  --cyan:#2eade3;
  --cyan-deep:#1f8fd6;
  --heading:#1d5a82;
  --text:#6a6a6a;
  --rule:#dcdcdc;
  --white:#ffffff;
  --band:#f3f3f3;
  --hero-a:#6aaee0;
  --hero-b:#b9dbf2;
}
*{box-sizing:border-box;margin:0;padding:0}
html,body{width:1200px;height:1071px;overflow:hidden;background:var(--white);font-family:"Ubuntu",sans-serif;color:var(--text)}
.page{position:relative;width:1200px;height:1071px}
.abs{position:absolute}

.main-nav{left:0;top:0;width:1200px;height:26px;background:linear-gradient(#0e4a6e,var(--navy-dark))}
.main-nav ul{list-style:none;position:absolute;right:189px;top:6px;display:flex;gap:20px;font-size:14px;color:#d6ecf7}
.main-nav li.active{color:var(--white);font-weight:700}
.main-nav li.current{position:relative}
.main-nav li.current::after{content:"";position:absolute;left:50%;bottom:-7px;margin-left:-4px;border:4px solid transparent;border-bottom-color:var(--cyan)}
.sub-nav{left:0;top:26px;width:1200px;height:24px;background:var(--cyan)}
.sub-nav ul{list-style:none;position:absolute;right:189px;top:4px;display:flex;gap:18px;font-size:12.5px;color:#0b3b5a}

.brand{left:183px;top:104px;display:flex;align-items:center;gap:8px;font-size:20px;font-weight:500;color:var(--cyan)}
.brand-dot{width:14px;height:14px;border-radius:50%;background:var(--navy)}
.hero-rule{left:0;top:138px;width:1200px;height:4px;background:var(--navy)}

.hero{left:0;top:142px;width:1200px;height:376px;background:linear-gradient(160deg,var(--hero-a) 0%,var(--hero-b) 100%)}
.hero-title{right:188px;top:174px;text-align:right;color:var(--navy);font-weight:700;line-height:1}
.hero-title .l1{font-size:29px}
.hero-title .l2{font-size:58px;letter-spacing:-1px;margin:2px 0 -2px}
.hero-title .l3{font-size:29px}
.slider-tab{left:183px;top:491px;width:107px;height:27px;background:var(--white);border-radius:6px 6px 0 0;display:flex;gap:6px;align-items:center;justify-content:center}
.slider-tab span{width:12px;height:12px;border-radius:50%;background:#d3d3d3}
.slider-tab span.on{background:var(--cyan)}

h2{font-weight:500;color:var(--heading)}
.about{left:183px;top:536px;width:300px}
.about h2{font-size:17px;margin-bottom:7px}
.about p{font-size:11px;line-height:14px}
.btn-small{display:inline-block;margin-top:6px;background:var(--cyan);color:var(--white);font-size:10px;padding:1px 3px;border-radius:2px}

.partners{left:534px;top:536px}
.partners h2{font-size:17px}
.badges{display:flex;gap:18px;align-items:center;margin-top:20px}
.badge{background:#222;height:40px}
.badge.grey{background:#bdbdbd}

.divider{left:183px;top:660px;width:829px;height:1px;background:var(--rule)}
.offer-title{left:183px;top:672px;font-size:18px}

.card{top:704px;width:176px;height:134px;border-radius:6px;background:linear-gradient(#3ac6ec,var(--cyan-deep));border:1px solid #1b82c4;color:var(--white);text-align:center}
.card h3{font-weight:400;font-size:20px;margin-top:44px;margin-bottom:8px;color:#eaf7fd}
.card ul{list-style:none;text-align:left;font-size:11px;line-height:14px;display:inline-block}
.card li::before{content:"▫ ";}
.arrow{top:752px}

.loan-copy{left:183px;top:846px;width:307px;font-size:11px;line-height:14px}
.copy-rule{left:183px;top:917px;width:313px;height:1px;background:var(--rule)}
.borrow-btn{left:182px;top:928px;width:316px;height:23px;border:2px solid #9a9a9a;border-radius:12px;font-size:15px;color:#444;text-align:center;line-height:19px;letter-spacing:.5px;background:linear-gradient(#fff,#eee)}

.help-art{left:588px;top:885px;width:115px;height:62px;background:#e4eef5;border-radius:8px}
.support-btn{left:620px;top:955px;width:54px;height:14px;background:var(--cyan);color:var(--white);font-size:10px;text-align:center;line-height:14px;border-radius:2px}

.contact{left:793px;top:847px;display:flex;gap:10px;font-size:11px;line-height:14px}
.phone-ico{width:34px;height:34px;background:var(--navy);border-radius:3px;display:flex;align-items:center;justify-content:center}
.contact strong{font-weight:400;color:var(--navy)}

.newsletter{left:793px;top:891px;width:218px;height:74px;border:3px solid #dbe9f4;background:#f7fbfe;padding:6px 8px}
.newsletter h4{display:flex;gap:6px;align-items:center;font-weight:400;font-size:13px;color:var(--navy)}
.newsletter p{font-size:7.5px;line-height:9px;color:#888;margin-top:4px}
.nl-form{display:flex;margin-top:4px;font-size:8px}
.nl-form .field{flex:1;background:var(--white);padding:3px 10px;color:#333;font-style:italic}
.nl-form .go{width:72px;background:var(--cyan);color:var(--white);text-align:center;padding:3px 0}

.band{left:0;top:973px;width:1200px;height:28px;background:var(--band)}
.footer{left:0;top:1001px;width:1200px;height:70px;background:var(--navy)}
.foot-nav{left:184px;top:1014px;list-style:none;display:flex;gap:17px;font-size:12px;color:#e3eef5}
.foot-rule{left:183px;top:1038px;width:325px;height:1px;background:#2d6284}
.foot-legal{left:183px;top:1043px;font-size:9px;line-height:12px;color:#c6d9e6}
.social{right:191px;top:1013px;text-align:right;font-size:9.5px;color:var(--white)}
.social .icons{display:flex;gap:4px;margin-top:3px;justify-content:flex-end}
.social .icons span{width:16px;height:16px;border-radius:2px;background:#2e7fbf;border:1px solid #cfe3f1}
</style>
</head>
<body>
<div class="page">

  <nav class="abs main-nav"><ul><li class="active">Home</li><li class="current">Services</li><li>About us</li><li>FAQ</li><li>Contact us</li></ul></nav>
  <nav class="abs sub-nav"><ul><li>Home loans</li><li>Investment loans</li><li>Refinancing loans</li><li>Business loans</li></ul></nav>

  <div class="abs brand"><span class="brand-dot"></span>corvellalending</div>
  <div class="abs hero-rule"></div>

  <div class="abs hero" role="img" aria-label="Hero photo: a hand dropping a coin into a piggy bank outdoors"></div>
  <div class="abs hero-title"><div class="l1">Finding the</div><div class="l2">right loan</div><div class="l3">for you</div></div>
  <div class="abs slider-tab"><span></span><span></span><span></span><span class="on"></span><span></span></div>

  <section class="abs about">
    <h2>Corvella Lending</h2>
    <p>At Corvella Lending we work hard to find the right loan for our customers. We do that because we<br>are backed by sound industry knowledge, professional experience and a great customer service<br>approach.</p>
    <span class="btn-small">Read More</span>
  </section>

  <section class="abs partners">
    <h2>Our Partners</h2>
    <div class="badges">
      <div class="badge" style="width:38px"></div>
      <div class="badge grey" style="width:60px;height:30px"></div>
      <div class="badge grey" style="width:80px;height:30px"></div>
      <div class="badge" style="width:48px"></div>
      <div class="badge grey" style="width:80px;height:30px"></div>
      <div class="badge" style="width:48px"></div>
    </div>
  </section>

  <div class="abs divider"></div>
  <h2 class="abs offer-title">We offer a unique approach to help you find the right:</h2>

  <svg class="abs arrow" style="left:186px" width="16" height="32" viewBox="0 0 16 32"><path d="M13 2 3 16l10 14" fill="none" stroke="#d4d4d4" stroke-width="3"/></svg>
  <div class="abs card" style="left:225px"><h3>Home Loan</h3><ul><li>Home buyers</li><li>First home buyers</li><li>Over 20 lenders</li></ul></div>
  <div class="abs card" style="left:414px"><h3>Investment Loan</h3><ul><li>Property investment loans</li><li>Interest only loans</li></ul></div>
  <div class="abs card" style="left:604px"><h3>Refinancing</h3><ul><li>Refinancing for the best rate</li><li>Upsizing or downsizing</li><li>Change from a variable<br>&nbsp;&nbsp;to a fixed rate</li></ul></div>
  <div class="abs card" style="left:793px"><h3 style="margin-top:42px">Business Finance</h3><ul><li>Long term</li><li>Short term</li><li>Equipment and Leasing</li></ul></div>
  <svg class="abs arrow" style="left:992px" width="16" height="32" viewBox="0 0 16 32"><path d="M3 2l10 14L3 30" fill="none" stroke="#d4d4d4" stroke-width="3"/></svg>

  <p class="abs loan-copy">There are many different loan products in the marketplace. Corvella Lending has access to a wide panel of lenders which means we can access bank and non-bank lenders that meet the individual needs of our customers.</p>
  <div class="abs copy-rule"></div>
  <div class="abs borrow-btn">Find out how much you could borrow</div>

  <div class="abs help-art" role="img" aria-label="Decorative lettering: Happy to Help"></div>
  <div class="abs support-btn">Support</div>

  <div class="abs contact">
    <div class="phone-ico"><svg width="18" height="22" viewBox="0 0 18 22"><path d="M5 1 2 3c-2 5 3 15 9 18l3-2-3-5-3 1C6 12 5 9 5 7l3-1z" fill="#fff"/></svg></div>
    <p>Contact Corvella Lending today on:<br><strong>1800 555 010</strong> to find out more.</p>
  </div>

  <div class="abs newsletter">
    <h4><svg width="22" height="15" viewBox="0 0 22 15"><rect x="1" y="1" width="20" height="13" fill="none" stroke="#0a3d5e"/><path d="M1 1l10 8 10-8" fill="none" stroke="#0a3d5e"/></svg>Subscribe Newsletters</h4>
    <p>Get in touch, we do not spam. Lorem Ipsum is simply dummy text of the printing and typesetting indus-</p>
    <div class="nl-form"><span class="field">yourname@mailbox.test</span><span class="go">Subscribe</span></div>
  </div>

  <div class="abs band"></div>
  <footer class="abs footer"></footer>
  <ul class="abs foot-nav"><li>Home</li><li>Services</li><li>About us</li><li>FAQ</li><li>Contact us</li><li>Sitemap</li></ul>
  <div class="abs foot-rule"></div>
  <p class="abs foot-legal">Copyright@corvellalending | All rights reserved.<br>Privacy Policy | About us | Terms &amp; Conditions</p>
  <div class="abs social">Stay in contact with us<div class="icons"><span></span><span></span><span></span><span></span><span></span></div></div>

</div>
</body>
</html>
```